Simple and clean poster/flyer design needed for public speaker!

SIMPLE AND CLEAN DESIGN NEEDED FOR POSTER/FLYER

I AM a public speaker based in London (www.tobiaskernwald.com)
and I would like to have a custom-made flyer/poster
(preferably in adobe CS4 template format) that I con customize (just changing the text) for my various speeches, topics and locations

I am looking for something very simple and clean.
NO extravagance or crowded poster, but a rather beautiful clean and eye-catching design that clearly informs people what i am talking about, where and when.

Go to my website www.tobiaskernwald.com
to see the colour scheme and style that I like
my poster should be like the website, similar colours, logo, clean, simple and clear.

Summary

(1) simple and clean design
(2) design that fits my brand (see website)
(3) clear and eye-catching to promote my speeches
(4) customizable for my various talks, by simply chancing the text (Please Adobe Photoshop CS4 template format)
(5)in A3, A4, A5, A6 sizes, so i can use it for both flyers and small posters

ADDITIONS

BIG BOLD HEADLINE TO GRAP ATTENTION, greatest prominence

sub headline to explain, smaller than the headline, but still prominent on the poster

just a few bullet points to list the benefits and answer the “whats in for me”-question
this is for people who are already interested and continue reading, medium prominence.

WHERE, WHEN, HOW MUCH-information, in the lower section of the poster, little text, but clearly visible

only one point of CONTACT on my poster “www.tobiaskernwald.com”, bit big and clear so that it is very prominent

little text, effectively used
LESS IS MORE
Updates

contact me regarding logo files and any questions you may have!

for the logo files go to

https://secure.dropvaultly.com/fs/v.aspx?v=41958b2d703c9ea1f6d2

click on the folder "logo pack" to see the files

eps
jpg
png
photoshop
TIF

thanks for your interest. hope to see great designs!
I am really looking forward to it
if you have any questions, please do not hesitate to ask

Kind Regards
Tobias
 

• Simple, clean design, text sparingly used.

• The mood should be light-hearted, calm, bright, simple and friendly, comic like

• a lot of white space, calling more attention to the content

• a light blue, dark blue, white and black colour scheme as seen on the homepage (www.tobiaskernwald.com) please use the exact same colours as seen on the homepage.

White being most predominant, 2 different blue used to highlight something, black for text on white background.

• One graphic would be cool, as long as it is blue. It could be waves-like graphic, or something like the white pattern in the background, in my case just in blue on white background > http://www.lumenquietharbor.org/., I do not mean exactly this graphic and not that crowded but a simple single graphic in blue as long as it fits the theme and feel of my poster

Top o f the poster

• (a )One short bold headline (TALK TITLE) with a sub-headline below it (hook)

• or (b) headline as question (…....?) and below sub-headline offering the solution (my talk ;-) of course)

• 3 benefits as on homepage, that I can adapt for each talk (bottom right of my start site “what are you looking for?” either blue on white, or as in the page white on blue...whatever looks better and fits the design). Not sure how that looks, and if to include it!

• the bottom of the poster will have “Where”-information “when”-information “ticket price” info

• contact at the very bottom...for more into or to purchase tickets (my website and email)

If you have any questions or need clarification please write me!

Requirements
Must have
• lot of white space
• less is more - simple design
• little text, little graphics- only used when necessary to greatest effect.
• light, friendly, modern feel
• blue-color scheme

```html
<!DOCTYPE html>
<html lang="en">
<head>
<meta charset="utf-8">
<title>What are you looking for? – Tobias Kernwald talk poster</title>
<link rel="stylesheet" href="https://fonts.googleapis.com/css2?family=Questrial&family=Mulish:wght@600;800;900&family=Archivo+Black&display=swap">
<style>
  :root {
    --sky-top: #4f9fdc;
    --sky-mid: #9ccbee;
    --sky-low: #dcecf7;
    --white: #ffffff;
    --brand-blue: #3aa0c0;
    --ink: #0a0a0a;
    --deep-blue: #0b5b7c;
    --bright-blue: #2cb8e6;
    --pale-blue: #a8d4e2;
  }
  * { margin: 0; padding: 0; box-sizing: border-box; }
  html, body { width: 1008px; height: 1200px; overflow: hidden; background: var(--white); }
  .poster { position: relative; width: 1008px; height: 1200px; overflow: hidden; background: var(--white); font-family: "Questrial", sans-serif; }

  .sky {
    position: absolute; left: 0; top: 0; width: 1008px; height: 465px;
    background:
      radial-gradient(ellipse 260px 160px at 430px 120px, rgba(255,255,255,0.85), rgba(255,255,255,0) 70%),
      radial-gradient(ellipse 200px 70px at 900px 60px, rgba(255,255,255,0.7), rgba(255,255,255,0) 70%),
      radial-gradient(ellipse 220px 60px at 120px 100px, rgba(255,255,255,0.6), rgba(255,255,255,0) 70%),
      linear-gradient(180deg, var(--sky-top) 0%, var(--sky-mid) 35%, var(--sky-low) 62%, var(--white) 100%);
  }

  .headline {
    position: absolute; left: 0; top: 282px; width: 1008px; text-align: center;
    font-family: "Mulish", sans-serif; font-weight: 800; font-size: 62px; letter-spacing: -0.5px;
    color: var(--brand-blue); line-height: 1;
  }
  .headline .you { color: var(--ink); font-weight: 900; }

  .subheadline {
    position: absolute; left: 0; top: 378px; width: 1008px; text-align: center;
    font-size: 35px; letter-spacing: 3px; color: var(--brand-blue); line-height: 1;
  }

  .benefits {
    position: absolute; left: 79px; top: 512px; list-style: none;
    font-size: 26px; line-height: 35px; color: var(--brand-blue);
  }

  .waves { position: absolute; left: 0; top: 0; width: 1008px; height: 1200px; }

  .brand-mark {
    position: absolute; left: 318px; top: 636px;
    display: flex; align-items: center; gap: 7px;
    font-size: 20px; color: var(--brand-blue); line-height: 1;
  }
  .brand-mark .dot { width: 12px; height: 12px; border-radius: 50%; background: var(--brand-blue); }

  .details {
    position: absolute; left: 79px; top: 946px; list-style: none;
    font-size: 27px; line-height: 42px; color: var(--white);
  }

  .contact {
    position: absolute; left: 0; top: 1114px; width: 1008px; text-align: center;
    font-family: "Archivo Black", sans-serif; font-size: 36px; letter-spacing: 13.5px;
    color: var(--ink); line-height: 1;
  }
</style>
</head>
<body>
<main class="poster">
  <div class="sky" role="img" aria-label="Bright blue sky with soft white clouds and sun rays"></div>

  <h1 class="headline">“what are <span class="you">YOU</span> looking for?”</h1>
  <p class="subheadline">practical spirituality to transform your life</p>

  <ul class="benefits">
    <li>inner peace &amp; calm</li>
    <li>improved self-esteem</li>
    <li>greater purpose &amp; meaning in life</li>
  </ul>

  <svg class="waves" viewBox="0 0 1008 1200" aria-hidden="true">
    <defs>
      <radialGradient id="deepWave" cx="0.45" cy="0.75" r="0.75">
        <stop offset="0" stop-color="var(--bright-blue)"/>
        <stop offset="0.55" stop-color="#1a8db5"/>
        <stop offset="1" stop-color="var(--deep-blue)"/>
      </radialGradient>
    </defs>
    <path class="wave-light" d="M300,672 C540,680 760,760 1008,835 L1008,1200 L0,1200 Z" fill="var(--pale-blue)"/>
    <path class="wave-deep" d="M0,664 C180,646 330,664 470,735 C640,825 790,990 1008,1130 L1008,1200 L0,1200 Z" fill="url(#deepWave)"/>
  </svg>

  <div class="brand-mark"><span class="dot"></span><span>tobias</span></div>

  <ul class="details">
    <li>when: date</li>
    <li>where: location</li>
    <li>ticket: price</li>
  </ul>

  <p class="contact">www.tobiaskernwald.com</p>
</main>
</body>
</html>
```